Business card for Chiropractic clinics needs reworked / redesigned

The business card in attachment was designed 10 years ago. It is in need of an update.
We have 2 clinics:
VELDHOVE KLINIEK & VELDHOVE KLINIEK NOORD
Only one address needs to be on the card for doctors that only work in one clinic and two addresses need to be on the card for the doctors that work in both clinics.

Target Market(s)

patients/referrers

Industry/Entity Type

Medical

Contact Information for Business Card

Logo (in full or zoomed-in)
Clinic Name
Doctor name and title
clinic address, website, tel, email

Font styles to use
Sans Serif

Colors

Designer to choose colors to be used in the design.

Requirements
Must have
• Good contrast/readability
• We like modern minimalistic designs
• The Bcard needs to project our very high standard of proficiency/professionalism
Should not have
• Not curly
• Not to much colours

```html
<!DOCTYPE html>
<html lang="nl">
<head>
<meta charset="utf-8">
<title>Veldhove Kliniek – visitekaartje</title>
<link rel="stylesheet" href="https://fonts.googleapis.com/css2?family=Fira+Sans+Condensed:wght@400;600;700&display=swap">
<style>
  :root {
    --forest: #2c4a3a;
    --forest-light: #6f9a82;
    --amber: #e6a63c;
    --paper: #ffffff;
    --ink: #2c4a3a;
    --ink-soft: #3c4a43;
    --stage: #e9ebe8;
  }
  * { margin: 0; padding: 0; box-sizing: border-box; }
  html, body {
    width: 1200px; height: 1200px; overflow: hidden;
    background: var(--stage);
    font-family: "Fira Sans Condensed", "Arial Narrow", sans-serif;
  }
  .sheet {
    position: relative; width: 1200px; height: 1200px;
  }
  .card {
    position: absolute; left: 150px; width: 900px; height: 514px;
    overflow: hidden; border-radius: 4px;
    box-shadow: 0 14px 36px rgba(0,0,0,0.18);
  }
  .card--front { top: 60px; background: var(--forest); }
  .card--back { top: 626px; background: var(--paper); }

  .card__art { position: absolute; inset: 0; width: 100%; height: 100%; }

  /* front */
  .front-brand {
    position: absolute; left: 330px; top: 196px; text-align: right;
  }
  .front-brand__name {
    color: var(--paper); font-weight: 700; font-size: 50px;
    letter-spacing: 2px; line-height: 1;
  }
  .front-brand__web {
    color: var(--paper); font-size: 24px; font-weight: 400;
    letter-spacing: 1px; margin-top: 10px; opacity: 0.92;
  }

  /* back */
  .doctor {
    position: absolute; left: 410px; right: 40px; top: 44px;
  }
  .doctor__row {
    display: flex; justify-content: space-between; align-items: flex-end;
    padding-bottom: 8px; border-bottom: 2px solid var(--amber);
  }
  .doctor__name {
    color: var(--ink); font-weight: 700; font-size: 30px; letter-spacing: 0.5px;
  }
  .doctor__title {
    color: var(--amber); font-weight: 600; font-size: 22px; letter-spacing: 1px;
  }
  .doctor__contact {
    list-style: none; text-align: right; margin-top: 12px;
    color: var(--ink-soft); font-size: 20px; line-height: 1.35;
  }
  .clinics {
    position: absolute; left: 420px; right: 40px; bottom: 46px;
    display: flex; gap: 26px;
  }
  .clinic {
    flex: 1; color: var(--ink-soft); font-size: 20px; line-height: 1.35;
  }
  .clinic + .clinic { border-left: 2px solid var(--amber); padding-left: 22px; }
  .clinic__name {
    color: var(--ink); font-weight: 700; font-size: 20px; letter-spacing: 0.3px;
  }
</style>
</head>
<body>
<main class="sheet">

  <section class="card card--front" aria-label="Voorkant visitekaartje">
    <svg class="card__art" viewBox="0 0 900 514" aria-hidden="false">
      <defs>
        <radialGradient id="front-motif-fill" cx="0.35" cy="0.6" r="0.7">
          <stop offset="0" stop-color="#6f9a82" stop-opacity="0.55"/>
          <stop offset="1" stop-color="#6f9a82" stop-opacity="0"/>
        </radialGradient>
      </defs>
      <rect x="0" y="170" width="420" height="344" fill="url(#front-motif-fill)"
            role="img" aria-label="Decoratief ruggengraatmotief"/>
    </svg>
    <div class="front-brand">
      <div class="front-brand__name">VELDHOVE KLINIEK</div>
      <div class="front-brand__web">www.veldhovekliniek.be</div>
    </div>
  </section>

  <section class="card card--back" aria-label="Achterkant visitekaartje">
    <svg class="card__art" viewBox="0 0 900 514">
      <defs>
        <radialGradient id="back-motif-fill" cx="0.5" cy="0.6" r="0.6">
          <stop offset="0" stop-color="#6f9a82" stop-opacity="0.5"/>
          <stop offset="1" stop-color="#6f9a82" stop-opacity="0"/>
        </radialGradient>
      </defs>
      <polygon points="0,0 330,0 370,514 0,514" fill="var(--forest)"/>
      <rect x="20" y="80" width="340" height="420" fill="url(#back-motif-fill)"
            role="img" aria-label="Decoratief ruggengraatmotief"/>
      <polygon points="330,0 358,0 398,514 370,514" fill="var(--amber)"/>
    </svg>

    <div class="doctor">
      <div class="doctor__row">
        <span class="doctor__name">Lieven MAERTENS D.C.</span>
        <span class="doctor__title">CHIROPRACTOR</span>
      </div>
      <ul class="doctor__contact">
        <li>0.470 12 34 56</li>
        <li>info@veldhovekliniek.be</li>
        <li>www.veldhovekliniek.be</li>
      </ul>
    </div>

    <div class="clinics">
      <address class="clinic" style="font-style:normal">
        <div class="clinic__name">VELDHOVE KLINIEK</div>
        <div>Lindenlaan 48</div>
        <div>09 210 45 80</div>
        <div>veldhovekliniek.be</div>
      </address>
      <address class="clinic" style="font-style:normal">
        <div class="clinic__name">VELDHOVE KLINIEK NOORD</div>
        <div>Kerkstraat 17</div>
        <div>09 360 72 14</div>
        <div>veldhovekliniek-noord.be</div>
      </address>
    </div>
  </section>

</main>
</body>
</html>
```